TriVex Business Card Design - double sided -plumbing local plumbing company

We have a Plumbing company where the design was create through Sketch Hive. We would now like a business card designed as well. We want it to be in the colour version of the logo.

Details below for the card.

Phone Number: 0438 615 247
Email: info@trivexplumbing.example.au
Website: https://trivexplumbing.example.au
We really want a sophisticated design that stand out from the other- informative and timeless.

Target Market(s)

local Canberra market

Industry/Entity Type

Plumbing, gas fitting, hot water

Contact Information for Business Card

Phone number, email, logo and "Supplying all your heating, cooling and hot water needs"

Requirements
Must have
• bust be colourful, must also be though about it being printed on a magnet. must Vex with the logo - I dont want the logo and information chucked onto a white canvas I would prefer it to be smooth and look purposeful

```html
<!DOCTYPE html>
<html lang="en">
<head>
<meta charset="utf-8">
<title>TriVex Plumbing – Business Card</title>
<link rel="stylesheet" href="https://fonts.googleapis.com/css2?family=Montserrat:wght@600;800&display=swap">
<style>
  :root {
    --page: #ffffff;
    --blue-light: #1ea6e0;
    --blue-mid: #1380c6;
    --blue-deep: #0c4d98;
    --white: #ffffff;
    --amber: #f9a93a;
    --wave: rgba(255, 255, 255, 0.08);
  }
  * { margin: 0; padding: 0; box-sizing: border-box; }
  html, body {
    width: 1200px; height: 1200px; overflow: hidden;
    background: var(--page);
    font-family: "Montserrat", sans-serif;
  }
  .card {
    position: absolute; left: 118px; width: 971px; height: 554px;
    overflow: hidden;
    background: linear-gradient(100deg, var(--blue-light) 0%, var(--blue-mid) 50%, var(--blue-deep) 100%);
  }
  .card--front { top: 36px; }
  .card--back { top: 624px; }
  .card__waves { position: absolute; inset: 0; width: 100%; height: 100%; }

  .brand-name {
    position: absolute; color: var(--white); font-weight: 800;
    text-align: center; line-height: 1; text-transform: uppercase;
  }
  .card--front .brand-name {
    left: 0; right: 0; top: 214px; font-size: 84px; letter-spacing: 2px;
  }
  .card--front .brand-name .brand-name__sub {
    display: block; margin-top: 14px; font-size: 36px; letter-spacing: 16px;
  }
  .card--back .brand-name {
    right: 44px; top: 32px; font-size: 25px; letter-spacing: 0.5px;
  }
  .card--back .brand-name .brand-name__sub {
    display: block; margin-top: 2px; font-size: 11px; letter-spacing: 4.5px;
  }

  .illustration { position: absolute; }
  .illustration--tap {
    left: 340px; top: 4px; width: 188px; height: 222px;
    border-radius: 40% 40% 30% 30%;
    background: radial-gradient(ellipse at 50% 45%, rgba(220, 240, 255, 0.55), rgba(120, 190, 235, 0.15) 70%, transparent 75%);
  }
  .illustration--splash {
    left: 232px; top: 332px; width: 512px; height: 120px; border-radius: 50%;
    background: radial-gradient(ellipse at 50% 50%, rgba(235, 248, 255, 0.8), rgba(150, 210, 245, 0.35) 55%, transparent 72%);
  }

  .tagline {
    position: absolute; left: 0; right: 0; top: 222px;
    text-align: center; color: var(--white);
    font-weight: 800; font-size: 42px; line-height: 56px;
    font-variant: small-caps; letter-spacing: -0.5px;
  }
  .tagline__accent { color: var(--amber); }

  .contact {
    position: absolute; left: 34px; right: 34px; top: 494px;
    display: flex; justify-content: space-between; align-items: center;
    color: var(--white); font-weight: 800; font-size: 16px; letter-spacing: 0.8px;
    text-transform: uppercase;
  }
  .contact__item { display: flex; align-items: center; gap: 8px; }
  .contact__icon { width: 20px; height: 20px; fill: none; stroke: var(--white); stroke-width: 1.6; }
  .contact__icon--solid { fill: var(--white); stroke: none; }
</style>
</head>
<body>

<section class="card card--front" aria-label="Business card front">
  <svg class="card__waves" viewBox="0 0 971 554" preserveAspectRatio="none" aria-hidden="true">
    <path d="M0 150 C120 260 260 230 330 160 C420 70 520 60 620 120 C720 180 820 60 971 0 L0 0 Z" fill="var(--wave)"/>
    <path d="M0 554 L0 470 C120 380 220 400 300 440 C420 500 560 420 700 350 C820 290 900 320 971 300 L971 554 Z" fill="var(--wave)"/>
  </svg>
  <h1 class="brand-name">TriVex<span class="brand-name__sub">Plumbing</span></h1>
</section>

<section class="card card--back" aria-label="Business card back">
  <svg class="card__waves" viewBox="0 0 971 554" preserveAspectRatio="none" aria-hidden="true">
    <path d="M0 150 C120 260 260 230 330 160 C420 70 520 60 620 120 C720 180 820 60 971 0 L0 0 Z" fill="var(--wave)"/>
    <path d="M0 554 L0 470 C120 380 220 400 300 440 C420 500 560 420 700 350 C820 290 900 320 971 300 L971 554 Z" fill="var(--wave)"/>
  </svg>
  <div class="illustration illustration--tap" role="img" aria-label="Chrome tap with a water drop falling from the spout"></div>
  <div class="illustration illustration--splash" role="img" aria-label="Water drop splashing into a rippling pool"></div>

  <p class="brand-name">TriVex<span class="brand-name__sub">Plumbing</span></p>

  <h2 class="tagline">
    Supplying all your <span class="tagline__accent">heating,</span><br>
    <span class="tagline__accent">cooling</span> and <span class="tagline__accent">hot water</span> needs
  </h2>

  <div class="contact">
    <span class="contact__item">
      <svg class="contact__icon contact__icon--solid" viewBox="0 0 24 24" aria-hidden="true"><path d="M6.6 10.8a15 15 0 0 0 6.6 6.6l2.2-2.2a1 1 0 0 1 1-.25 11.4 11.4 0 0 0 3.6.57 1 1 0 0 1 1 1V20a1 1 0 0 1-1 1A17 17 0 0 1 3 4a1 1 0 0 1 1-1h3.5a1 1 0 0 1 1 1c0 1.25.2 2.45.57 3.57a1 1 0 0 1-.25 1z"/></svg>
      0438 615 247
    </span>
    <span class="contact__item">
      <svg class="contact__icon" viewBox="0 0 24 24" aria-hidden="true"><rect x="2.5" y="5" width="19" height="14"/><path d="M2.5 5l9.5 8 9.5-8M2.5 19l7-7M21.5 19l-7-7"/></svg>
      info@trivexplumbing.example.au
    </span>
    <span class="contact__item">
      <svg class="contact__icon" viewBox="0 0 24 24" aria-hidden="true"><circle cx="12" cy="12" r="9.5"/><ellipse cx="12" cy="12" rx="4.5" ry="9.5"/><path d="M2.5 12h19M4 7h16M4 17h16M12 2.5v19"/></svg>
      trivexplumbing.example.au
    </span>
  </div>
</section>

</body>
</html>
```